Business card design needed

I need a business card for my Sydney Painting Business, that specialises in painting High -end residential homes. i want the design to look clean, modern and edgy. i also want a logo next to the RL Decorating, using RLD together.

Industry/Entity Type

Residential

Contact Information for Business Card

RL Decorating (business name),LIC 871536K, Rob Lindqvist, robert.lindqvist@brushmail.example, mobile 0419352807

```html
<!DOCTYPE html>
<html lang="en">
<head>
<meta charset="utf-8">
<title>RL Decorating – Business Card</title>
<link rel="stylesheet" href="https://fonts.googleapis.com/css2?family=Questrial&display=swap">
<style>
  :root {
    --canvas-bg: #161616;
    --card-white: #ffffff;
    --card-dark: #262626;
    --card-dark-deep: #1c1c1c;
    --accent-orange: #f39a12;
    --ink-grey: #4a4a4a;
    --ink-light: #f2f2f2;
  }
  * { box-sizing: border-box; margin: 0; padding: 0; }
  html, body {
    width: 1200px;
    height: 844px;
    overflow: hidden;
    background: var(--canvas-bg);
    font-family: "Questrial", "Century Gothic", sans-serif;
  }
  .canvas {
    width: 1200px;
    height: 844px;
    display: flex;
    align-items: center;
    justify-content: center;
    gap: 40px;
  }
  .card {
    position: relative;
    width: 540px;
    height: 309px;
    overflow: hidden;
    border-radius: 3px;
  }

  /* Back side: dark all over with centred brand */
  .card--back .card__pattern {
    position: absolute;
    inset: 0;
    background: linear-gradient(160deg, var(--card-dark) 0%, var(--card-dark-deep) 100%);
  }
  .brand {
    position: absolute;
    display: flex;
    flex-direction: column;
    align-items: flex-start;
    line-height: 1;
  }
  .brand__mark {
    color: var(--accent-orange);
    font-size: 30px;
    letter-spacing: 2px;
    margin-left: 48px;
    margin-bottom: 4px;
  }
  .brand__name {
    font-size: 30px;
  }
  .card--back .brand {
    left: 150px;
    top: 118px;
  }
  .card--back .brand__name { color: var(--ink-light); }

  /* Front side: white upper half, dark toothed lower half */
  .card--front { background: var(--card-white); }
  .card--front .card__pattern {
    position: absolute;
    left: 0;
    top: 0;
    width: 540px;
    height: 309px;
  }
  .card--front .brand {
    left: 268px;
    top: 60px;
  }
  .card--front .brand__name { color: var(--ink-grey); }

  .contact {
    position: absolute;
    left: 30px;
    top: 178px;
    list-style: none;
    color: var(--ink-light);
    font-size: 15px;
    line-height: 24px;
  }
  .contact__label {
    display: inline-block;
    width: 20px;
    color: var(--accent-orange);
    font-weight: bold;
  }
</style>
</head>
<body>
  <main class="canvas">
    <section class="card card--back" aria-label="Business card back">
      <div class="card__pattern" role="img" aria-label="Dark checkered diamond pattern background"></div>
      <div class="brand">
        <span class="brand__mark">RLD</span>
        <span class="brand__name">RL Decorating</span>
      </div>
    </section>

    <section class="card card--front" aria-label="Business card front">
      <svg class="card__pattern" viewBox="0 0 540 309" role="img" aria-label="Dark checkered diamond pattern with toothed upper edge">
        <defs>
          <linearGradient id="dark-fill" x1="0" y1="0" x2="1" y2="1">
            <stop offset="0" stop-color="#2a2a2a"/>
            <stop offset="1" stop-color="#1c1c1c"/>
          </linearGradient>
        </defs>
        <polygon fill="url(#dark-fill)" points="0,150 15,135 30,150 45,135 60,150 75,135 90,150 105,135 120,150 135,135 150,150 165,135 180,150 195,135 210,150 225,135 240,150 255,135 270,150 285,135 300,150 315,135 330,150 345,135 360,150 375,135 390,150 405,135 420,150 435,135 450,150 465,135 480,150 495,135 510,150 525,135 540,150 540,309 0,309"/>
      </svg>
      <div class="brand">
        <span class="brand__mark">RLD</span>
        <span class="brand__name">RL Decorating</span>
      </div>
      <ul class="contact">
        <li><span class="contact__label">#</span>LIC 871536K, Rob Lindqvist</li>
        <li><span class="contact__label">M</span>0419352807</li>
        <li><span class="contact__label">E</span>robert.lindqvist@brushmail.example</li>
      </ul>
    </section>
  </main>
</body>
</html>
```